Biz Card for Harrowfield Property Partners - HFPP

Harrowfield Property Partners is a commercial real estate acquisitions firm. We buy commercial property and need to raise capital from investors for each deal we buy. The vibe needs to be: give us your money, we will multiply it.
Our website: www.hfldpp.com
Competitors are: https://marvenby.com/, https://trellumpartners.com/, http://www.quorvantcapital.com/
Target Market(s)
High Net Worth Individuals, Bankers, Insurance Companies, Commercial Real Estate Brokers.
Industry/Entity Type
Investment Banking
Contact Information for Business Card
Name, Title, Addess, Cell#, Office#, email, website
Requirements
Must have
- use one of our logos. See website for look and feel: www.hfldpp.com
Nice to have
- see website: www.hfldpp.com

```html
<!DOCTYPE html>
<html lang="en">
<head>
<meta charset="utf-8">
<title>Harrowfield Property Partners — Business Card</title>
<link href="https://fonts.googleapis.com/css2?family=Montserrat:wght@400;500;600&family=Quicksand:wght@400;500&display=swap" rel="stylesheet">
<style>
  :root {
    --backdrop: #2b2c2f;
    --navy: #0f2f48;
    --navy-deep: #0a2236;
    --navy-light: #123d5c;
    --accent-blue: #1c74b8;
    --paper: #ffffff;
    --ink-grey: #6f7479;
    --ink-soft: #9aa0a6;
  }
  * { box-sizing: border-box; margin: 0; padding: 0; }
  html, body {
    width: 1200px; height: 960px; overflow: hidden;
    background: var(--backdrop);
  }
  .canvas { position: relative; width: 1200px; height: 960px; }

  .card {
    position: absolute;
    width: 620px; height: 354px;
    border-radius: 22px;
    overflow: hidden;
  }

  /* Back side */
  .card-back {
    left: 140px; top: 90px;
    background: linear-gradient(160deg, var(--navy-light) 0%, var(--navy-deep) 100%);
  }
  .back-mark {
    position: absolute; left: 50%; top: 150px;
    width: 200px; height: 200px; margin: -100px 0 0 -100px;
    border-radius: 50%;
    background: linear-gradient(135deg, var(--accent-blue) 0%, #0b3556 55%, #061626 100%);
    display: flex; flex-direction: column; align-items: center; justify-content: center;
    color: var(--paper);
    font-family: "Montserrat", sans-serif; font-weight: 400;
    text-align: center;
  }
  .back-mark .name-main { font-size: 16px; letter-spacing: 2.4px; }
  .back-mark .name-sub { font-size: 8.5px; letter-spacing: 2.2px; margin-top: 6px; }
  .back-url {
    position: absolute; left: 0; right: 0; top: 284px;
    text-align: center;
    font-family: "Montserrat", sans-serif; font-weight: 500;
    font-size: 13px; letter-spacing: 5px;
    color: var(--paper);
  }
  .back-url strong { font-weight: 600; }

  /* Front side */
  .card-front {
    left: 440px; top: 510px;
    background: var(--paper);
  }
  .name-band {
    position: absolute; left: 0; top: 132px;
    width: 300px; height: 66px;
    background: var(--navy);
    padding: 13px 0 0 62px;
    color: var(--paper);
  }
  .person-name {
    font-family: "Montserrat", sans-serif; font-weight: 600;
    font-size: 20px; letter-spacing: 0.3px;
  }
  .person-title {
    font-family: "Montserrat", sans-serif; font-weight: 400;
    font-size: 13px; margin: 2px 0 0 14px;
  }
  .brand-circle {
    position: absolute; left: 262px; top: 92px;
    width: 92px; height: 92px; border-radius: 50%;
    background: var(--paper);
    border: 5px solid var(--navy);
  }
  .brand-name {
    position: absolute; left: 368px; top: 104px;
    font-family: "Montserrat", sans-serif; font-weight: 400;
    color: var(--navy);
  }
  .brand-name .name-main { font-size: 22px; letter-spacing: 3px; line-height: 1; }
  .brand-name .name-sub { font-size: 9.5px; letter-spacing: 2.6px; margin-top: 8px; }

  .address {
    position: absolute; right: 40px; top: 200px;
    text-align: right;
    font-family: "Quicksand", sans-serif; font-weight: 400; font-style: normal;
    font-size: 13.5px; line-height: 18px;
    color: var(--ink-grey);
  }
  .contacts {
    position: absolute; left: 96px; top: 250px;
    list-style: none;
    font-family: "Quicksand", sans-serif; font-weight: 500;
    font-size: 14px; line-height: 20px;
    color: var(--ink-grey);
  }
  .contacts li { display: flex; align-items: center; gap: 9px; }
  .contacts svg { width: 11px; height: 11px; fill: var(--navy); flex: none; }
</style>
</head>
<body>
<main class="canvas">

  <section class="card card-back" aria-label="Card back">
    <div class="back-mark">
      <span class="name-main">HARROWFIELD</span>
      <span class="name-sub">PROPERTY PARTNERS</span>
    </div>
    <p class="back-url">WWW.<strong>HFLDPP</strong>.COM</p>
  </section>

  <section class="card card-front" aria-label="Card front">
    <div class="name-band">
      <p class="person-name">DANIEL CARVER</p>
      <p class="person-title">President</p>
    </div>
    <div class="brand-circle"></div>
    <div class="brand-name">
      <p class="name-main">HARROWFIELD</p>
      <p class="name-sub">PROPERTY PARTNERS</p>
    </div>

    <address class="address">
      48 Verano Way<br>
      Suite 710<br>
      Larkspur Bay<br>
      FL 30418
    </address>

    <ul class="contacts">
      <li>
        <svg viewBox="0 0 12 12" aria-hidden="true"><path d="M2.4 0.8l1.8-.3 1 2.5-1.2.9c.6 1.4 1.6 2.4 3 3l.9-1.2 2.5 1-.3 1.8c-.1.6-.6 1-1.2 1C4.4 9.4 1.4 6.4 1.4 2c0-.6.4-1.1 1-1.2z"/></svg>
        (555) 214-3098
      </li>
      <li>
        <svg viewBox="0 0 12 12" aria-hidden="true"><path d="M3 0.5h6a1 1 0 0 1 1 1v9a1 1 0 0 1-1 1H3a1 1 0 0 1-1-1v-9a1 1 0 0 1 1-1zm.4 1.5v7h5.2V2zM6 9.6a.6.6 0 1 0 0 1.2.6.6 0 0 0 0-1.2z"/></svg>
        (555) 306-7712
      </li>
      <li>
        <svg viewBox="0 0 12 12" aria-hidden="true"><path d="M1 2.5h10v7H1zm.9.9v.3L6 6.5l4.1-2.8v-.3z"/></svg>
        info@hfldpp.com
      </li>
      <li>
        <svg viewBox="0 0 12 12" aria-hidden="true"><path d="M6 .8a5.2 5.2 0 1 0 0 10.4A5.2 5.2 0 0 0 6 .8zm0 1.3c.7.8 1.1 2 1.2 3.3H4.8C4.9 4.1 5.3 2.9 6 2.1zM2.1 6.6h1.5c.1 1.2.4 2.2 1 3A4 4 0 0 1 2.1 6.6zm0-1.2a4 4 0 0 1 2.5-3c-.6.8-.9 1.8-1 3zm3.9 4.5c-.7-.8-1.1-2-1.2-3.3h2.4C7.1 7.9 6.7 9.1 6 9.9zm1.4-.3c.6-.8.9-1.8 1-3h1.5a4 4 0 0 1-2.5 3zm1-4.2c-.1-1.200-.4-2.2-1-3a4 4 0 0 1 2.5 3z"/></svg>
        hfldpp.com
      </li>
    </ul>
  </section>

</main>
</body>
</html>
```